Flying Trapeze School needs a Poster Design

Our company is the Pacific Leisure Institute of Skyward Motion (PLISM)
We need a poster design to promote our flying trapeze classes during Summer. Our classes are perfect for the whole family (6+ years).
You can learn to perform tricks in the air and be caught mid flight, just like being in the circus.
We would like the poster to be bright and eye catching yet easy to read.
The design should communicate the location and contact details and appeal to families.

Target Market(s)

Families

Industry/Entity Type

School

Requirements
Must have
• The poster must have the company name, location, contact details and our logo as well as the Harbourlight Precinct logo (the harbourlight precinct logo can be smaller and located on the bottom of the poster).
Company name: Pacific Leisure Institute of Skyward Motion (PLISM) The acronym can be used instead of writing the whole name.
Location: Gallowfield
Contact: Ph 0481 226 903, email info@plism-example.net.au, web www.swingloftexample.net.au
Nice to have
• We have attached some photos that could be used.

```html
<!DOCTYPE html>
<html lang="en">
<head>
<meta charset="utf-8">
<title>Flying Trapeze Summer Classes – PLISM</title>
<link rel="stylesheet" href="https://fonts.googleapis.com/css2?family=Alfa+Slab+One&family=Libre+Franklin:wght@400;700&display=swap">
<style>
  :root {
    --page: #ffffff;
    --forest: #1c3a27;
    --night: #000000;
    --lime: #c6f03a;
    --white: #ffffff;
    --photo-light: #d9d2b4;
    --photo-mid: #8c8f6a;
    --badge: #a9d6ea;
  }
  html, body {
    margin: 0;
    width: 1200px;
    height: 900px;
    overflow: hidden;
    background: var(--page);
  }
  .poster {
    position: absolute;
    left: 335px;
    top: 14px;
    width: 509px;
    height: 874px;
    background: var(--forest);
    font-family: "Libre Franklin", Arial, sans-serif;
    text-align: center;
  }
  .hero-photo {
    position: absolute;
    left: 0;
    top: 0;
    width: 509px;
    height: 312px;
    background: radial-gradient(ellipse 60% 65% at 50% 45%, var(--photo-light) 0%, var(--photo-mid) 50%, var(--forest) 100%);
  }
  .headline {
    position: absolute;
    left: 0;
    top: 330px;
    width: 100%;
    margin: 0;
    font-family: "Alfa Slab One", "Rockwell", serif;
    font-weight: 400;
    color: var(--lime);
    font-size: 92px;
    line-height: 78px;
    letter-spacing: 1px;
  }
  .subhead {
    position: absolute;
    left: 0;
    top: 482px;
    width: 100%;
    margin: 0;
    font-family: "Alfa Slab One", "Rockwell", serif;
    font-weight: 400;
    color: var(--white);
    font-size: 42px;
    line-height: 48px;
    letter-spacing: 1px;
  }
  .venue {
    position: absolute;
    left: 0;
    top: 530px;
    width: 100%;
    margin: 0;
    font-weight: 700;
    color: var(--lime);
    font-size: 22px;
    line-height: 28px;
  }
  .info-band {
    position: absolute;
    left: 0;
    top: 576px;
    width: 100%;
    height: 235px;
    background: var(--night);
    color: var(--lime);
  }
  .pitch {
    margin: 12px 0 0;
    font-size: 11px;
    line-height: 15px;
  }
  .brand-mark {
    position: absolute;
    left: 0;
    top: 92px;
    width: 100%;
    display: flex;
    justify-content: center;
    align-items: center;
    gap: 10px;
    font-weight: 700;
    font-size: 22px;
    color: var(--lime);
  }
  .brand-mark .dot {
    width: 40px;
    height: 40px;
    border-radius: 50%;
    background: var(--lime);
  }
  .company {
    position: absolute;
    left: 0;
    top: 158px;
    width: 100%;
    margin: 0;
    font-weight: 700;
    font-size: 17px;
  }
  .contact {
    position: absolute;
    left: 0;
    top: 183px;
    width: 100%;
    margin: 0;
    font-size: 12px;
    line-height: 15px;
  }
  .partner-badge {
    position: absolute;
    left: 193px;
    top: 844px;
    width: 128px;
    height: 22px;
    background: var(--badge);
  }
</style>
</head>
<body>
  <main class="poster">
    <div class="hero-photo" role="img" aria-label="Photo of a young girl flying on a trapeze bar, held by her legs, smiling"></div>
    <h1 class="headline">Flying<br>Trapeze</h1>
    <h2 class="subhead">Summer Classes</h2>
    <p class="venue">at the Gallowfield</p>
    <section class="info-band">
      <p class="pitch">Perfect for the whole family (6+ years).<br>Learn to perform tricks in the air and be caught in mid flight<br>just like being in the circus.</p>
      <div class="brand-mark"><span class="dot"></span><span>PLISM</span></div>
      <p class="company">Pacific Leisure Institute of Skyward Motion</p>
      <p class="contact">Phone: 0481 226 903<br>email: info@plism-example.net.au<br>web: www.swingloftexample.net.au</p>
    </section>
    <div class="partner-badge" role="img" aria-label="Harbourlight Precinct partner badge"></div>
  </main>
</body>
</html>
```